Dental Office Needs an Innovative Postcard Redesign

We need an updated and innovative look to our existing postcard. We would like to see creative new elements and new ways of laying out the existing offers. Please use the same colors to maintain brand consistency. Postcard size is 6 inches in height and 11 inches in width.

Industry/Entity Type

Dental

Requirements
Must have
• Stay with the brand colors and font. visit website if needed

```html
<!DOCTYPE html>
<html lang="en">
<head>
<meta charset="utf-8">
<title>Bright Day Dental Postcard</title>
<link href="https://fonts.googleapis.com/css2?family=Open+Sans:wght@300;400&family=Arimo:wght@400;700&display=swap" rel="stylesheet">
<style>
:root{
  --ink:#231f20;
  --cyan:#3ec1e8;
  --navy:#1d5f93;
  --sky:#1a9ac9;
  --sky-light:#5cc3e6;
  --steel:#8ea3c6;
  --orange:#f47b3a;
  --paper:#ffffff;
  --backdrop:#e6e6e6;
}
*{margin:0;padding:0;box-sizing:border-box}
html,body{width:1200px;height:1000px;overflow:hidden}
body{background:var(--backdrop);font-family:"Arimo",Arial,sans-serif;position:relative}
.postcard{position:absolute;left:177px;width:844px;height:459px;background:var(--paper);overflow:hidden}
.postcard--front{top:31px}
.postcard--back{top:503px}
.header-bands,.footer-bands{position:absolute;left:0;width:844px}
.header-bands{top:0;height:125px}
.brand{position:absolute;left:30px;top:14px;color:var(--paper)}
.brand__name{font-family:"Open Sans",Arial,sans-serif;font-weight:300;font-size:42px;letter-spacing:1px;line-height:1}
.brand__tagline{font-family:"Open Sans",Arial,sans-serif;font-weight:400;font-size:14px;letter-spacing:2.4px;margin-top:8px}
.contact{position:absolute;right:18px;top:18px;text-align:right}
.contact__address{color:var(--paper);font-weight:700;font-size:14.5px}
.contact__web{color:var(--cyan);font-weight:700;font-size:12.5px;letter-spacing:1.6px;margin-top:3px}
.family-photo{position:absolute;left:363px;top:70px;width:481px;height:335px;background:linear-gradient(160deg,#f4f4f4 0%,#d9d5d2 45%,#b7aea7 100%)}
.offer-list{position:absolute;left:24px;top:128px;list-style:none}
.offer{display:flex;align-items:center;height:43px;font-size:14px;color:var(--ink);line-height:1.2}
.offer__icon{width:28px;height:28px;margin-right:12px;flex:none}
.offer .hl{color:var(--navy);font-weight:700}
.offer .price{color:var(--orange);font-weight:700;font-size:15px}
.offer sup{font-size:8px}
.footer-bands{bottom:0;height:100px}
.phone{position:absolute;left:30px;display:flex;align-items:center;color:var(--paper);font-weight:700;font-size:35px}
.phone svg{margin-right:16px}
.postcard--front .phone{top:407px}
.postcard--back .phone{top:390px;font-size:45px}
.fine-print{position:absolute;top:403px;width:212px;color:var(--paper);font-size:6px;line-height:1.35}
.fine-print--a{left:374px}
.fine-print--b{left:627px}
.schedule{position:absolute;left:602px;width:242px;height:74px}
.postcard--front .schedule{top:320px}
.postcard--back .schedule{top:55px}
.schedule__banner{position:absolute;left:60px;top:18px;width:182px;height:42px;background:var(--orange);display:flex;align-items:center;padding-left:28px;color:var(--paper)}
.schedule__small{font-size:7.5px;letter-spacing:.8px;line-height:1.15}
.schedule__big{font-size:21px;font-weight:700;margin-left:4px}
.schedule__seal{position:absolute;left:0;top:0}
.section-bar{position:absolute;top:132px;height:45px;background:var(--navy);color:var(--paper);font-size:22px;font-weight:700;display:flex;align-items:center;justify-content:center;letter-spacing:.3px}
.section-bar--implant{left:0;width:362px}
.section-bar--crown{left:471px;width:373px}
.illustration{position:absolute}
.illustration--implant{left:25px;top:190px;width:190px;height:140px;background:linear-gradient(180deg,#f1f1f1 0%,#e8d8c4 60%,#e9c9a4 100%)}
.illustration--crown{left:648px;top:188px;width:172px;height:158px;background:linear-gradient(160deg,#f4f7fa 0%,#d7e2ec 100%)}
.price-block{position:absolute;top:190px;width:150px;color:var(--ink)}
.price-block--implant{left:233px}
.price-block--crown{left:475px}
.price-block__lead{font-size:18px}
.price-block__amount{font-size:36px;font-weight:700;color:var(--navy);line-height:.95}
.price-block__note{font-size:12px;line-height:14.5px;margin-top:6px}
.mail-panel{position:absolute;left:489px;top:349px;width:339px;height:100px;background:var(--paper);border:5px solid var(--sky);border-radius:14px}
</style>
</head>
<body>

<!-- FRONT -->
<section class="postcard postcard--front">
  <div class="family-photo" role="img" aria-label="Smiling family of four, two parents and two young boys"></div>

  <svg class="header-bands" viewBox="0 0 844 125" aria-hidden="true">
    <polygon points="0,0 844,0 844,62 0,95" fill="#231f20"/>
    <polygon points="0,95 844,62 844,76 0,110" fill="#8ea3c6"/>
    <polygon points="0,110 844,76 844,82 0,118" fill="#c5d0e2"/>
  </svg>
  <div class="brand">
    <div class="brand__name">BRIGHT DAY</div>
    <div class="brand__tagline">FAMILY | COSMETIC | IMPLANTS</div>
  </div>
  <div class="contact">
    <div class="contact__address">1630 N. Maple Grove Road, Suite 210, Mesa AZ 85201</div>
    <div class="contact__web">WWW.BRIGHTDAYMESA.COM</div>
  </div>

  <ul class="offer-list">
    <li class="offer">
      <svg class="offer__icon" viewBox="0 0 28 28"><rect x="2" y="2" width="24" height="24" fill="none" stroke="#231f20" stroke-width="2"/><path d="M9 9h10v6l-2 6h-2l-1-4-1 4h-2l-2-6z" fill="none" stroke="#231f20" stroke-width="1.6"/></svg>
      <span><span class="hl">FREE</span> Emergency exam and X Rays.<sup>1</sup></span>
    </li>
    <li class="offer">
      <svg class="offer__icon" viewBox="0 0 28 28"><path d="M14 2 L26 12 V26 H2 V12 Z" fill="none" stroke="#231f20" stroke-width="2"/><text x="14" y="22" font-size="7" font-weight="700" text-anchor="middle" font-family="Arimo,Arial,sans-serif">NEW</text></svg>
      <span><span class="hl">NEW PATIENCE OFFER</span> <span class="price">25%</span><br>Includes cleaning, X Rays and exam.<sup>2</sup></span>
    </li>
    <li class="offer">
      <svg class="offer__icon" viewBox="0 0 28 28"><circle cx="14" cy="14" r="12" fill="none" stroke="#231f20" stroke-width="2"/><text x="14" y="20" font-size="16" font-weight="700" text-anchor="middle" font-family="Arimo,Arial,sans-serif">?</text></svg>
      <span><span class="hl">NEW INSURANCE?</span> <span class="price">NO PROBLEM</span><br>Ask about our in-house discount plan.</span>
    </li>
    <li class="offer">
      <svg class="offer__icon" viewBox="0 0 28 28"><circle cx="10" cy="10" r="7" fill="none" stroke="#231f20" stroke-width="2"/><line x1="5" y1="15" x2="2" y2="24" stroke="#231f20" stroke-width="2"/><path d="M16 12h9v6l-2 7h-2l-1-4-1 4h-2l-1-7z" fill="none" stroke="#231f20" stroke-width="1.6"/></svg>
      <span><span class="hl">FREE</span> Second Opinion<sup>3</sup> &amp; Denture consultation<sup>4</sup></span>
    </li>
    <li class="offer">
      <svg class="offer__icon" viewBox="0 0 28 28"><path d="M5 6h18v9l-3 10h-3l-3-6-3 6H8L5 15z" fill="none" stroke="#231f20" stroke-width="2"/></svg>
      <span><span class="hl">ALL PORCELAIN</span> Caps/Crowns &amp; Veneers<sup>5</sup><br>starting at <span class="price">$597</span></span>
    </li>
    <li class="offer">
      <svg class="offer__icon" viewBox="0 0 28 28"><rect x="8" y="2" width="12" height="7" rx="2" fill="none" stroke="#231f20" stroke-width="2"/><rect x="6" y="11" width="16" height="3" fill="#231f20"/><path d="M10 16h8M10 20h8M11 24h6" stroke="#231f20" stroke-width="2"/></svg>
      <span>Dental Implant and Crown<sup>6</sup> starting at <span class="price">$1997</span></span>
    </li>
  </ul>

  <svg class="footer-bands" viewBox="0 0 844 100" aria-hidden="true">
    <polygon points="0,22 844,0 844,100 0,100" fill="#1a9ac9"/>
    <polygon points="360,100 844,40 844,100" fill="#2b86c2"/>
    <polygon points="0,22 844,0 844,6 0,30" fill="#5cc3e6"/>
  </svg>
  <div class="phone">
    <svg width="24" height="40" viewBox="0 0 24 40"><rect x="2" y="2" width="20" height="36" rx="3" fill="none" stroke="#fff" stroke-width="2.5"/><line x1="2" y1="8" x2="22" y2="8" stroke="#fff" stroke-width="2"/><line x1="2" y1="31" x2="22" y2="31" stroke="#fff" stroke-width="2"/></svg>
    480-555-0142
  </div>
  <p class="fine-print fine-print--a">1-New patients only, call for details.<br>2-Value of $285. In the absence of periodontal disease. New patients only. Not valid with any other offer. Limited time offer. Call for details.<br>3-X-rays may be taken, additional fees may apply. Call for details.</p>
  <p class="fine-print fine-print--b">4-With or without dental implants. Made in the USA. Call for details.<br>5-Crown build up not included. Have insurance? No problem! Contract insurance fees apply. Made in the USA. Call for details.<br>6-Implant, crown, standard abutment. Have insurance? No problem! Made in the USA. Call for details.</p>

  <div class="schedule">
    <div class="schedule__banner"><span class="schedule__small">SCHEDULE YOUR<br>APPOINTMENT</span><span class="schedule__big">TODAY</span></div>
    <svg class="schedule__seal" width="74" height="74" viewBox="0 0 74 74" aria-hidden="true">
      <circle cx="37" cy="37" r="36" fill="#1d5f93"/>
      <circle cx="37" cy="37" r="31" fill="#3ec1e8"/>
      <circle cx="37" cy="37" r="26" fill="#fff"/>
      <rect x="24" y="26" width="26" height="22" rx="2" fill="none" stroke="#f47b3a" stroke-width="2"/>
      <line x1="24" y1="32" x2="50" y2="32" stroke="#f47b3a" stroke-width="2"/>
      <line x1="30" y1="23" x2="30" y2="29" stroke="#f47b3a" stroke-width="2"/>
      <line x1="44" y1="23" x2="44" y2="29" stroke="#f47b3a" stroke-width="2"/>
      <path d="M32 40l4 4 7-7" fill="none" stroke="#1d5f93" stroke-width="2"/>
    </svg>
  </div>
</section>

<!-- BACK -->
<section class="postcard postcard--back">
  <svg class="header-bands" viewBox="0 0 844 125" aria-hidden="true">
    <polygon points="0,0 844,0 844,62 0,95" fill="#231f20"/>
    <polygon points="0,95 844,62 844,76 0,110" fill="#8ea3c6"/>
    <polygon points="0,110 844,76 844,82 0,118" fill="#c5d0e2"/>
  </svg>
  <div class="brand">
    <div class="brand__name">BRIGHT DAY</div>
    <div class="brand__tagline">FAMILY | COSMETIC | IMPLANTS</div>
  </div>
  <div class="contact">
    <div class="contact__address">1630 N. Maple Grove Road, Suite 210, Mesa AZ 85201</div>
    <div class="contact__web">WWW.BRIGHTDAYMESA.COM</div>
  </div>

  <div class="schedule">
    <div class="schedule__banner"><span class="schedule__small">SCHEDULE YOUR<br>APPOINTMENT</span><span class="schedule__big">TODAY</span></div>
    <svg class="schedule__seal" width="74" height="74" viewBox="0 0 74 74" aria-hidden="true">
      <circle cx="37" cy="37" r="36" fill="#1d5f93"/>
      <circle cx="37" cy="37" r="31" fill="#3ec1e8"/>
      <circle cx="37" cy="37" r="26" fill="#fff"/>
      <rect x="24" y="26" width="26" height="22" rx="2" fill="none" stroke="#f47b3a" stroke-width="2"/>
      <line x1="24" y1="32" x2="50" y2="32" stroke="#f47b3a" stroke-width="2"/>
      <line x1="30" y1="23" x2="30" y2="29" stroke="#f47b3a" stroke-width="2"/>
      <line x1="44" y1="23" x2="44" y2="29" stroke="#f47b3a" stroke-width="2"/>
      <path d="M32 40l4 4 7-7" fill="none" stroke="#1d5f93" stroke-width="2"/>
    </svg>
  </div>

  <div class="section-bar section-bar--implant">IMPLANT PLACEMENT</div>
  <div class="section-bar section-bar--crown">CAPS/CROWNS &amp; VENEERS</div>

  <div class="illustration illustration--implant" role="img" aria-label="Illustration of a dental implant, abutment and crown set in the jawbone"></div>
  <div class="price-block price-block--implant">
    <div class="price-block__lead">Starting at</div>
    <div class="price-block__amount">$799</div>
    <p class="price-block__note">Addittional fee for implant crown and abutment. Have insurance? No problem! Contact insurance fees apply. Made in USA. Call for details.</p>
  </div>

  <div class="price-block price-block--crown">
    <div class="price-block__lead">Starting at</div>
    <div class="price-block__amount">$549</div>
    <p class="price-block__note">Crown built up not included. Have insurance? No problem! Contract insurance fee apply. Made in the USA. Calls for details.</p>
  </div>
  <div class="illustration illustration--crown" role="img" aria-label="Illustration of a porcelain crown above a prepared tooth and a finished crowned tooth"></div>

  <svg class="footer-bands" viewBox="0 0 844 100" aria-hidden="true">
    <polygon points="0,10 844,0 844,100 0,100" fill="#1a9ac9"/>
    <polygon points="420,100 844,30 844,100" fill="#2b86c2"/>
    <polygon points="0,4 844,-6 844,2 0,14" fill="#5cc3e6"/>
  </svg>
  <div class="phone">
    <svg width="30" height="54" viewBox="0 0 30 54"><rect x="2" y="2" width="26" height="50" rx="4" fill="none" stroke="#fff" stroke-width="3"/><line x1="2" y1="10" x2="28" y2="10" stroke="#fff" stroke-width="2.5"/><line x1="2" y1="43" x2="28" y2="43" stroke="#fff" stroke-width="2.5"/></svg>
    480-555-0142
  </div>
  <div class="mail-panel"></div>
</section>

</body>
</html>
```